Insurance Policy Administration Software Suite

Crestfield Data and Logic, Inc. ("CDLI") develops and deploys a suite of Insurance Policy Administration Systems, with add-on features. What we need is beautiful minimalist icons which look great on the PC desktop as well as on print. Our main product is the CoverageNest Platform, the add-ons are 1) ChartsNest Professional Reports Design; 2) AlertsNest Advanced Task Manager; 3) GatesNest Online Secure Self-Service Portals; and 4) FilesNest Document Management and Workflow.

I really like the new Veltrane FlowKits icons... I want minimalist that are not cartoonish, and don't overuse "plus" signs.

```html
<!DOCTYPE html>
<html lang="en">
<head>
<meta charset="utf-8">
<title>CoverageNest Add-on Suite</title>
<link href="https://fonts.googleapis.com/css2?family=Source+Sans+3:wght@400;700;800&display=swap" rel="stylesheet">
<style>
  :root {
    --bg: #ffffff;
    --ink: #0b0b0b;
    --navy: #3b3470;
    --lime: #93d95c;
    --yellow: #fdc60f;
    --amber: #f0b400;
    --orange: #f15a24;
    --sky: #0aa7e6;
    --green: #22a83f;
    --mist: #e3e6f0;
  }
  html, body {
    margin: 0;
    padding: 0;
    overflow: hidden;
  }
  .suite {
    position: relative;
    width: 1200px;
    height: 398px;
    background: var(--bg);
    font-family: "Source Sans 3", "Myriad Pro", sans-serif;
    color: var(--ink);
    overflow: hidden;
  }
  .product {
    position: absolute;
    top: 0;
    width: 260px;
    margin-left: -130px;
    text-align: center;
  }
  .product-icon {
    position: absolute;
    top: 98px;
    left: 75px;
    width: 110px;
    height: 110px;
    border-radius: 10px;
  }
  .icon-charts   { background: linear-gradient(135deg, var(--navy) 0%, var(--navy) 45%, var(--lime) 100%); }
  .icon-alerts   { background: linear-gradient(135deg, var(--yellow) 0%, var(--orange) 40%, var(--lime) 70%, var(--sky) 100%); }
  .icon-gates    { background: linear-gradient(135deg, var(--yellow) 0%, var(--amber) 60%, var(--green) 100%); }
  .icon-files    { background: linear-gradient(160deg, var(--amber) 0%, var(--yellow) 55%, var(--navy) 100%); }
  .product-name {
    position: absolute;
    top: 218px;
    left: 0;
    width: 100%;
    margin: 0;
    font-size: 28px;
    font-weight: 800;
    line-height: 30px;
    letter-spacing: 0.3px;
  }
  .product-tagline {
    position: absolute;
    top: 248px;
    left: 0;
    width: 100%;
    margin: 0;
    font-size: 19.5px;
    font-weight: 400;
    line-height: 28px;
    letter-spacing: 0.2px;
  }
</style>
</head>
<body>
<main class="suite">
  <section class="product" style="left:219px">
    <div class="product-icon icon-charts" role="img" aria-label="Icon: briefcase with a rising green arrow"></div>
    <h2 class="product-name">ChartsNest</h2>
    <p class="product-tagline">Professional Reports Design</p>
  </section>
  <section class="product" style="left:486px">
    <div class="product-icon icon-alerts" role="img" aria-label="Icon: gear inside a ring of four coloured cycle arrows"></div>
    <h2 class="product-name">AlertsNest</h2>
    <p class="product-tagline">Advanced Task Manager</p>
  </section>
  <section class="product" style="left:744px">
    <div class="product-icon icon-gates" role="img" aria-label="Icon: yellow bag with a green shield and tick"></div>
    <h2 class="product-name">GatesNest</h2>
    <p class="product-tagline">Online Secure Self-Service<br>Portals</p>
  </section>
  <section class="product" style="left:1002px">
    <div class="product-icon icon-files" role="img" aria-label="Icon: yellow folder linked to two sub-folders"></div>
    <h2 class="product-name">FilesNest</h2>
    <p class="product-tagline">Document Management<br>and Workflow</p>
  </section>
</main>
</body>
</html>
```